Marlow's Anvil BBQ Sauce Needs a Label

We are looking for a rustic label that would help our product stand out on a shelf. The company name is Marlow's Anvil. We are a new company looking to stand out on shelving with our amazing BBQ Sweet, Spicy and Rub. The label size needs to be 6.5" wide x 2.5" tall. I have taken a step in creating a label which is attached. This is just an idea for you to bring us an amazing retail ready look. On the left side of the label we need to have a 1 color flag with Made In USA. Also would need to have the address on the same side. Marlow's Anvil BBQ Sauce, Palm Hollow, FL 33999. The nutrition Facts are also needed. The information is correct but would need to be adjusted as to font and sizing. Image 7247 is what I have lightly put together and image 2495 is current logo on actual label. If you need any more guidance please let me know. Tobins ZestKing is an example of the pop we would like to see

Requirements
Must have
• Rustic Look
Nice to have
• Rustic look with a feeling similar to image 7247 that’s attached.
Should not have
• Same look as the original logo that’s on the actual label.

```html
<!DOCTYPE html>
<html lang="en">
<head>
<meta charset="utf-8">
<title>Marlow's Anvil BBQ Sauce – Label Set</title>
<link href="https://fonts.googleapis.com/css2?family=Alfa+Slab+One&family=Archivo:wght@400;700;900&display=swap" rel="stylesheet">
<style>
  :root{
    --paper-light:#f1e6c8;
    --paper-mid:#e6d3a8;
    --paper-edge:#cfb078;
    --stain:#c99f5e;
    --ink:#3a2421;
    --spicy:#d4263a;
    --rub:#e8722a;
    --sweet:#2ea33a;
    --badge:#f3ead2;
    --canvas:#ffffff;
  }
  *{box-sizing:border-box;margin:0;padding:0}
  html,body{width:1200px;height:927px;overflow:hidden;background:var(--canvas)}
  .defs{position:absolute;width:0;height:0}
  .label-sheet{position:relative;width:1200px;height:927px}
  .label{
    position:absolute;left:229px;width:742px;height:285px;
    background:
      radial-gradient(ellipse 160px 110px at 6% 8%,rgba(201,159,94,.55),transparent 70%),
      radial-gradient(ellipse 120px 80px at 22% 40%,rgba(201,159,94,.25),transparent 70%),
      radial-gradient(ellipse 140px 90px at 94% 90%,rgba(201,159,94,.35),transparent 70%),
      radial-gradient(ellipse 90px 70px at 70% 12%,rgba(201,159,94,.22),transparent 70%),
      radial-gradient(ellipse at 50% 55%,var(--paper-light) 0%,var(--paper-mid) 62%,var(--paper-edge) 100%);
    color:var(--ink);font-family:"Archivo",sans-serif;overflow:hidden;
  }
  .label--spicy{top:18px;--accent:var(--spicy)}
  .label--rub{top:318px;--accent:var(--rub)}
  .label--sweet{top:618px;--accent:var(--sweet)}
  .label__grain{position:absolute;inset:0;width:100%;height:100%;mix-blend-mode:multiply;opacity:.35;pointer-events:none}
  .label__band{position:absolute;left:0;right:0;bottom:0;height:12px;background:var(--ink)}
  .label__band::before{content:"";position:absolute;left:0;right:0;top:0;height:6px;background:var(--accent)}

  .origin{position:absolute;left:17px;top:192px}
  .origin__flag{display:block;width:69px;height:38px}
  .origin__made{font-weight:900;font-size:10px;letter-spacing:.2px;margin-top:3px}
  .origin__address{position:absolute;left:17px;top:251px;font-size:8px;line-height:10px}
  .origin__address strong{font-weight:900}

  .brand{position:absolute;left:210px;top:52px;width:320px;text-align:center}
  .brand__name{font-family:"Alfa Slab One",serif;font-size:38px;line-height:44px;letter-spacing:1px;color:var(--ink)}
  .variant{
    position:absolute;left:370px;top:222px;transform:translateX(-50%);
    padding:3px 20px;border:4px solid var(--ink);border-radius:4px;background:var(--badge);
    font-family:"Alfa Slab One",serif;font-size:14px;letter-spacing:1.5px;color:var(--accent)
  }

  .nutrition{
    position:absolute;left:595px;top:13px;width:132px;height:254px;border:1px solid var(--ink);
    padding:4px 5px;font-size:6.8px;line-height:1.22
  }
  .nutrition__title{font-weight:900;font-size:12.5px;line-height:12px;letter-spacing:.3px}
  .nutrition__row{display:flex;justify-content:space-between;border-top:.6px solid var(--ink);padding:2.1px 0}
  .nutrition__row--indent{padding-left:7px}
  .nutrition__row--plain{border-top:0;padding:0}
  .nutrition__rule-thick{height:4px;background:var(--ink);margin:2px 0}
  .nutrition__rule-mid{height:2px;background:var(--ink);margin:1px 0}
  .nutrition b{font-weight:700}
  .nutrition__note{font-size:4.8px;line-height:1.2;border-top:.6px solid var(--ink);padding-top:2px;margin-top:1px}
</style>
</head>
<body>
<svg class="defs" aria-hidden="true">
  <filter id="paper-grain">
    <feTurbulence type="fractalNoise" baseFrequency=".9" numOctaves="3" seed="4"/>
    <feColorMatrix values="0 0 0 0 .45  0 0 0 0 .33  0 0 0 0 .2  0 0 0 -1.1 1.05"/>
  </filter>
</svg>
<main class="label-sheet">

  <section class="label label--spicy">
    <svg class="label__grain" aria-hidden="true"><rect width="100%" height="100%" filter="url(#paper-grain)"/></svg>
    <div class="origin">
      <svg class="origin__flag" viewBox="0 0 69 38" role="img" aria-label="One-colour US flag">
        <g fill="#3a2421">
          <rect y="0" width="69" height="3"/><rect y="6" width="69" height="3"/><rect y="12" width="69" height="3"/>
          <rect y="18" width="69" height="3"/><rect y="24" width="69" height="3"/><rect y="30" width="69" height="3"/>
          <rect y="35" width="69" height="3"/><rect width="30" height="21"/>
        </g>
      </svg>
      <p class="origin__made">MADE IN USA</p>
    </div>
    <p class="origin__address"><strong>Marlow's Anvil BBQ Sauce,</strong><br>Palm Hollow, FL 33999</p>
    <div class="brand"><p class="brand__name">MARLOW'S<br>ANVIL<br>BBQ SAUCE</p></div>
    <span class="variant">SPICY</span>
    <div class="nutrition">
      <p class="nutrition__title">Nutrition Facts</p>
      <p>Serving Size 1 Tbsp. (18g)</p>
      <div class="nutrition__row nutrition__row--plain"><span>Servings Per Container</span><span>25</span></div>
      <div class="nutrition__rule-thick"></div>
      <p><b>Amount Per Serving</b></p>
      <div class="nutrition__row"><span><b>Calories</b> 25</span><span>Calories from Fat 0</span></div>
      <div class="nutrition__rule-mid"></div>
      <div class="nutrition__row nutrition__row--plain" style="justify-content:flex-end"><b>% Daily Value*</b></div>
      <div class="nutrition__row"><span><b>Total Fat</b> 0g</span><b>0%</b></div>
      <div class="nutrition__row nutrition__row--indent"><span>Saturated Fat 0g</span><b>0%</b></div>
      <div class="nutrition__row nutrition__row--indent"><span>Trans Fat 0g</span></div>
      <div class="nutrition__row"><span><b>Cholesterol</b> 0mg</span><b>0%</b></div>
      <div class="nutrition__row"><span><b>Sodium</b> 150mg</span><b>6%</b></div>
      <div class="nutrition__row"><span><b>Total Carbohydrate</b> 6g</span><b>2%</b></div>
      <div class="nutrition__row nutrition__row--indent"><span>Dietary Fiber 0g</span><b>0%</b></div>
      <div class="nutrition__row nutrition__row--indent"><span>Sugars 6g</span></div>
      <div class="nutrition__row"><span><b>Protein</b> 0.2g</span></div>
      <div class="nutrition__rule-thick"></div>
      <div class="nutrition__row nutrition__row--plain"><span>Vitamin A 1%</span><span>• Vitamin C 1%</span></div>
      <div class="nutrition__row"><span>Calcium 1%</span><span>• Iron 1%</span></div>
      <p class="nutrition__note">*Percent Daily Values are based on a 2,000 calorie diet. Your daily values may be higher or lower depending on your calorie needs</p>
    </div>
    <div class="label__band"></div>
  </section>

  <section class="label label--rub">
    <svg class="label__grain" aria-hidden="true"><rect width="100%" height="100%" filter="url(#paper-grain)"/></svg>
    <div class="origin">
      <svg class="origin__flag" viewBox="0 0 69 38" role="img" aria-label="One-colour US flag">
        <g fill="#3a2421">
          <rect y="0" width="69" height="3"/><rect y="6" width="69" height="3"/><rect y="12" width="69" height="3"/>
          <rect y="18" width="69" height="3"/><rect y="24" width="69" height="3"/><rect y="30" width="69" height="3"/>
          <rect y="35" width="69" height="3"/><rect width="30" height="21"/>
        </g>
      </svg>
      <p class="origin__made">MADE IN USA</p>
    </div>
    <p class="origin__address"><strong>Marlow's Anvil BBQ Sauce,</strong><br>Palm Hollow, FL 33999</p>
    <div class="brand"><p class="brand__name">MARLOW'S<br>ANVIL<br>BBQ SAUCE</p></div>
    <span class="variant">RUB</span>
    <div class="nutrition">
      <p class="nutrition__title">Nutrition Facts</p>
      <p>Serving Size 1 Tbsp. (18g)</p>
      <div class="nutrition__row nutrition__row--plain"><span>Servings Per Container</span><span>25</span></div>
      <div class="nutrition__rule-thick"></div>
      <p><b>Amount Per Serving</b></p>
      <div class="nutrition__row"><span><b>Calories</b> 25</span><span>Calories from Fat 0</span></div>
      <div class="nutrition__rule-mid"></div>
      <div class="nutrition__row nutrition__row--plain" style="justify-content:flex-end"><b>% Daily Value*</b></div>
      <div class="nutrition__row"><span><b>Total Fat</b> 0g</span><b>0%</b></div>
      <div class="nutrition__row nutrition__row--indent"><span>Saturated Fat 0g</span><b>0%</b></div>
      <div class="nutrition__row nutrition__row--indent"><span>Trans Fat 0g</span></div>
      <div class="nutrition__row"><span><b>Cholesterol</b> 0mg</span><b>0%</b></div>
      <div class="nutrition__row"><span><b>Sodium</b> 150mg</span><b>6%</b></div>
      <div class="nutrition__row"><span><b>Total Carbohydrate</b> 6g</span><b>2%</b></div>
      <div class="nutrition__row nutrition__row--indent"><span>Dietary Fiber 0g</span><b>0%</b></div>
      <div class="nutrition__row nutrition__row--indent"><span>Sugars 6g</span></div>
      <div class="nutrition__row"><span><b>Protein</b> 0.2g</span></div>
      <div class="nutrition__rule-thick"></div>
      <div class="nutrition__row nutrition__row--plain"><span>Vitamin A 1%</span><span>• Vitamin C 1%</span></div>
      <div class="nutrition__row"><span>Calcium 1%</span><span>• Iron 1%</span></div>
      <p class="nutrition__note">*Percent Daily Values are based on a 2,000 calorie diet. Your daily values may be higher or lower depending on your calorie needs</p>
    </div>
    <div class="label__band"></div>
  </section>

  <section class="label label--sweet">
    <svg class="label__grain" aria-hidden="true"><rect width="100%" height="100%" filter="url(#paper-grain)"/></svg>
    <div class="origin">
      <svg class="origin__flag" viewBox="0 0 69 38" role="img" aria-label="One-colour US flag">
        <g fill="#3a2421">
          <rect y="0" width="69" height="3"/><rect y="6" width="69" height="3"/><rect y="12" width="69" height="3"/>
          <rect y="18" width="69" height="3"/><rect y="24" width="69" height="3"/><rect y="30" width="69" height="3"/>
          <rect y="35" width="69" height="3"/><rect width="30" height="21"/>
        </g>
      </svg>
      <p class="origin__made">MADE IN USA</p>
    </div>
    <p class="origin__address"><strong>Marlow's Anvil BBQ Sauce,</strong><br>Palm Hollow, FL 33999</p>
    <div class="brand"><p class="brand__name">MARLOW'S<br>ANVIL<br>BBQ SAUCE</p></div>
    <span class="variant">SWEET</span>
    <div class="nutrition">
      <p class="nutrition__title">Nutrition Facts</p>
      <p>Serving Size 1 Tbsp. (18g)</p>
      <div class="nutrition__row nutrition__row--plain"><span>Servings Per Container</span><span>25</span></div>
      <div class="nutrition__rule-thick"></div>
      <p><b>Amount Per Serving</b></p>
      <div class="nutrition__row"><span><b>Calories</b> 25</span><span>Calories from Fat 0</span></div>
      <div class="nutrition__rule-mid"></div>
      <div class="nutrition__row nutrition__row--plain" style="justify-content:flex-end"><b>% Daily Value*</b></div>
      <div class="nutrition__row"><span><b>Total Fat</b> 0g</span><b>0%</b></div>
      <div class="nutrition__row nutrition__row--indent"><span>Saturated Fat 0g</span><b>0%</b></div>
      <div class="nutrition__row nutrition__row--indent"><span>Trans Fat 0g</span></div>
      <div class="nutrition__row"><span><b>Cholesterol</b> 0mg</span><b>0%</b></div>
      <div class="nutrition__row"><span><b>Sodium</b> 150mg</span><b>6%</b></div>
      <div class="nutrition__row"><span><b>Total Carbohydrate</b> 6g</span><b>2%</b></div>
      <div class="nutrition__row nutrition__row--indent"><span>Dietary Fiber 0g</span><b>0%</b></div>
      <div class="nutrition__row nutrition__row--indent"><span>Sugars 6g</span></div>
      <div class="nutrition__row"><span><b>Protein</b> 0.2g</span></div>
      <div class="nutrition__rule-thick"></div>
      <div class="nutrition__row nutrition__row--plain"><span>Vitamin A 1%</span><span>• Vitamin C 1%</span></div>
      <div class="nutrition__row"><span>Calcium 1%</span><span>• Iron 1%</span></div>
      <p class="nutrition__note">*Percent Daily Values are based on a 2,000 calorie diet. Your daily values may be higher or lower depending on your calorie needs</p>
    </div>
    <div class="label__band"></div>
  </section>

</main>
</body>
</html>
```